HTML Pretty Emails

We send out the attached emails to our clients as requeirements but they are so bland and boring.

We want pretty email to send out which i believe can be done through HTML.

I have attached what we currently have and what we want.

We have 4 brands hencce this contest is for 4 html emails templates with header and footer.

I would love to have a start your ORDER now button.

The branding can be seen on all the 4 websites.

4 Brands are:

I have attached 4 emails that we usually send out and these are prime examples of what we send our customers.

I have also attached an email from SUNNY D ECAL who i use for printing and i love their professional emails.

The emails you create should have as a bare minimum:
a) Header
b) Footer
c) Order now or start your order here button
d) Table showing the fees etc we charges as per email but much prettier.

You will provide me with 4 templates for each brand. The prettiest templates WIN!

Please feel free to be as creative as you want!

```html
<!DOCTYPE html>
<html lang="en">
<head>
<meta charset="utf-8">
<title>Belle Route Visa — Email Template</title>
<link href="https://fonts.googleapis.com/css2?family=Montserrat:wght@400;500;600;700&family=Mulish:wght@400;600;700&display=swap" rel="stylesheet">
<style>
:root{
  --red:#f2504b;
  --ink:#1f1f1f;
  --body:#3a3a3a;
  --muted:#8a8a8a;
  --faint:#c9c9c9;
  --panel:#f0f0f0;
  --white:#ffffff;
  --page:#e6eefa;
  --link:#2a5bd7;
  --rule:#dedede;
}
*{box-sizing:border-box;margin:0;padding:0}
html,body{width:1200px;height:4220px;overflow:hidden}
body{background:var(--page);font-family:"Mulish",sans-serif;color:var(--body);position:relative}
.abs{position:absolute}
.page-title{position:absolute;top:200px;left:0;width:1200px;text-align:center;font-family:"Montserrat",sans-serif;font-weight:700;font-size:30px;color:var(--ink);letter-spacing:.5px}
.page-title-rule{position:absolute;top:258px;left:565px;width:70px;height:3px;background:#3f6fd1}
.email{position:absolute;top:340px;left:20px;width:1160px;height:3530px;background:var(--white);box-shadow:0 10px 40px rgba(40,60,100,.12);overflow:hidden}
.section{position:absolute;left:0;width:1160px}

/* header */
.hero{top:0;height:652px;background:var(--white)}
.hero-band{position:absolute;left:0;top:0;width:580px;height:652px;background:var(--red)}
.brand{font-family:"Montserrat",sans-serif;font-weight:600;letter-spacing:1px}
.hero .brand{position:absolute;left:56px;top:26px;font-size:22px;color:var(--white)}
.nav{position:absolute;right:60px;top:26px;display:flex;gap:36px;align-items:center;font-size:20px;color:var(--ink)}
.card{position:absolute;left:54px;top:80px;width:1050px;height:490px;background:var(--white);box-shadow:0 12px 30px rgba(0,0,0,.12);overflow:hidden}
.card-watermark{position:absolute;left:20px;top:-30px;font-family:"Montserrat",sans-serif;font-weight:700;font-size:230px;letter-spacing:30px;color:#f3f3f3;white-space:nowrap}
.card-photo{position:absolute;right:0;top:0;width:560px;height:490px;background:linear-gradient(160deg,#ffffff 0%,#d4d4d4 45%,#4a4a4a 100%)}
.hero-title{position:absolute;left:56px;top:92px;font-family:"Montserrat",sans-serif;font-weight:700;font-size:52px;color:var(--ink)}
.hero-title span{color:var(--red)}
.hero-lede{position:absolute;left:54px;top:180px;width:460px;font-size:25px;line-height:40px;color:var(--ink)}
.btn{position:absolute;background:var(--red);color:var(--white);font-family:"Mulish",sans-serif;font-size:21px;display:flex;align-items:center;justify-content:center}
.hero .btn{left:48px;top:326px;width:186px;height:58px}
.follow{position:absolute;left:56px;top:604px;display:flex;align-items:center;gap:14px;font-size:19px;color:var(--white)}
.dot{width:12px;height:12px;border-radius:50%;background:var(--white)}

/* side markers */
.marker-num{position:absolute;font-family:"Montserrat",sans-serif;font-weight:600;font-size:28px;color:var(--faint)}
.marker-line{position:absolute;width:2px;background:var(--faint)}
.marker-word{position:absolute;font-family:"Montserrat",sans-serif;font-weight:600;font-size:26px;letter-spacing:8px;color:var(--faint);transform:rotate(-90deg);transform-origin:left top;white-space:nowrap}

/* pricing */
.pricing{top:652px;height:836px;background:var(--panel)}
.t{position:absolute;font-size:24px;line-height:30px}
.t-ink{color:var(--ink)}
.t-strong{font-weight:700;color:var(--ink)}
.heading-red{font-family:"Montserrat",sans-serif;font-weight:600;font-size:26px;color:var(--red);letter-spacing:.5px}
.rule{position:absolute;left:104px;width:948px;height:2px;background:var(--rule)}
.amount{position:absolute;right:108px;font-size:24px;color:var(--ink);text-align:right}

/* category */
.category{top:1488px;height:716px;background:var(--white)}
.heading-dark{font-family:"Montserrat",sans-serif;font-weight:600;font-size:27px;color:var(--ink);letter-spacing:1px}
.para{position:absolute;left:106px;width:900px;font-size:24px;line-height:40px;color:var(--ink);letter-spacing:.6px}
.para a{color:var(--link);text-decoration:none}
.choice{position:absolute;height:100px;background:var(--white);box-shadow:0 4px 16px rgba(0,0,0,.12);display:flex;align-items:center;justify-content:center;font-weight:700;font-size:23px;color:var(--ink)}
.choice.is-active{background:var(--red);color:#ffb4b1;font-weight:400}
.choice svg{position:absolute;left:50%;top:50%;transform:translate(-50%,-50%)}

/* faq */
.faq{top:2204px;height:614px;background:var(--panel)}
.q{position:absolute;left:104px;font-weight:700;font-size:23px;color:var(--ink)}
.toggle{position:absolute;right:108px;color:var(--red);font-size:28px;line-height:28px}
.faq .para a{color:var(--link)}

/* footer */
.footer{top:2818px;height:712px;background:var(--white)}
.footer-photo{position:absolute;right:0;top:0;width:442px;height:712px;background:linear-gradient(180deg,#f2f2f2 0%,#b5b5b5 40%,#6e6e6e 75%,#3c3c3c 100%)}
.footer .brand{position:absolute;left:104px;top:252px;font-size:42px;color:#444;font-weight:500;letter-spacing:2px}
.contact{position:absolute;left:0;top:336px;width:718px;height:376px;background:var(--red);color:var(--white)}
.contact-row{position:absolute;left:104px;display:flex;align-items:flex-start;gap:16px;font-size:23px;line-height:40px}
.contact-row svg{flex:none;margin-top:10px}
</style>
</head>
<body>

<div class="page-title">EMAIL TEMPLATE</div>
<div class="page-title-rule"></div>

<main class="email">

  <!-- header -->
  <header class="section hero">
    <div class="hero-band"></div>
    <div class="brand">BELLE ROUTE VISA</div>
    <nav class="nav">
      <span>Tourism</span><span>FAQs</span><span>Contact Us</span>
      <svg width="18" height="20" viewBox="0 0 18 20"><circle cx="9" cy="5" r="4.5" fill="#1f1f1f"/><path d="M1 20c0-5 3.5-8 8-8s8 3 8 8z" fill="#1f1f1f"/></svg>
    </nav>
    <div class="card">
      <div class="card-watermark">BELLE</div>
      <div class="card-photo" role="img" aria-label="Black and white photo of a tall iron lattice tower seen from below"></div>
      <h1 class="hero-title">France <span>Visas</span></h1>
      <p class="hero-lede">Make an appointment to get the best advices for visa application</p>
      <div class="btn">Order Now</div>
    </div>
    <div class="follow">Follow Us :
      <span class="dot"></span><span class="dot"></span><span class="dot"></span><span class="dot"></span>
    </div>
  </header>

  <!-- pricing -->
  <section class="section pricing">
    <div class="marker-num" style="left:42px;top:78px">01</div>
    <div class="marker-line" style="left:56px;top:118px;height:72px"></div>
    <div class="marker-word" style="left:42px;top:392px">PRICING</div>

    <p class="t t-ink" style="left:104px;top:78px">Hi,</p>
    <p class="t t-ink" style="left:104px;top:118px">Thanks for choosing Belle Route Visa</p>
    <h2 class="abs heading-red" style="left:106px;top:174px">SERVICE PRICING</h2>

    <p class="t" style="left:104px;top:236px;color:var(--muted)">Description</p>
    <p class="t amount" style="top:236px;color:var(--muted)">Amount</p>
    <div class="rule" style="top:280px"></div>

    <p class="t t-strong" style="left:104px;top:316px">You NOT married or dependant on a UK/EU National</p>
    <p class="t" style="left:104px;top:356px">Including all the fees</p>
    <p class="t amount" style="top:316px">£ 210</p>
    <div class="rule" style="top:420px"></div>

    <p class="t t-strong" style="left:102px;top:456px">You are married or dependant on a UK/EU National</p>
    <p class="t" style="left:100px;top:494px">Including all the fees</p>
    <p class="t amount" style="top:456px">£ 155</p>
    <div class="rule" style="top:558px"></div>

    <p class="t t-strong" style="left:104px;top:594px">Emergency appointments within 3 days</p>
    <p class="t amount" style="top:594px">£ 50 / per hour</p>
    <div class="rule" style="top:656px"></div>

    <p class="t t-ink" style="left:106px;top:698px">Please mention your name and nationality</p>
    <p class="t t-ink" style="left:106px;top:738px">followed by FRANCE- DELAUNAY</p>
    <div class="btn" style="left:822px;top:698px;width:230px;height:58px;font-size:23px">Link Payment</div>
  </section>

  <!-- category -->
  <section class="section category">
    <h2 class="abs heading-dark" style="left:108px;top:72px">CHOOSE CATEGORY</h2>
    <p class="para" style="top:128px">Complete list of required documents are available on our website at <a href="#">www.belleroutevisa.example</a> or you can download the check lists from below based on your category</p>
    <p class="t t-strong" style="left:108px;top:272px;font-weight:600">Tourism</p>
    <div class="choice" style="left:108px;top:338px;width:280px">Married to UK/EU</div>
    <div class="choice is-active" style="left:438px;top:338px;width:282px">A Student
      <svg width="40" height="40" viewBox="0 0 40 40"><circle cx="20" cy="20" r="18" fill="none" stroke="#fff" stroke-width="2.5"/><path d="M20 11v15M14 21l6 6 6-6M13 29h14" fill="none" stroke="#fff" stroke-width="2.5" stroke-linecap="round" stroke-linejoin="round"/></svg>
    </div>
    <div class="choice" style="left:772px;top:338px;width:280px">Employed</div>
    <p class="t t-strong" style="left:108px;top:470px;font-weight:600">Business</p>
    <div class="choice" style="left:108px;top:536px;width:280px">Business Visa</div>

    <div class="marker-num" style="left:1080px;top:74px">02</div>
    <div class="marker-line" style="left:1102px;top:126px;height:62px"></div>
    <div class="marker-word" style="left:1086px;top:442px">CATEGORY</div>
  </section>

  <!-- faq -->
  <section class="section faq">
    <div class="marker-num" style="left:34px;top:72px">03</div>
    <div class="marker-line" style="left:54px;top:116px;height:70px"></div>
    <div class="marker-word" style="left:38px;top:330px">FAQs</div>

    <p class="t" style="left:106px;top:74px;color:var(--red);font-weight:600">What Next?</p>
    <span class="toggle" style="top:74px">−</span>
    <p class="para" style="top:126px;left:106px;letter-spacing:0;color:var(--body)">Please complete and email us this <a href="#">Questionnaire</a> so we can arrange your submission appointment. Alternatively, you can email us PDF of the application form you completed on VCS's</p>

    <p class="q" style="top:274px">What happens if I already have booked my Appointment?</p><span class="toggle" style="top:276px">+</span>
    <p class="q" style="top:332px">When is the appointment available?</p><span class="toggle" style="top:334px">+</span>
    <p class="q" style="top:392px">I already had a visa - do I need to give BIOMETRICS again?</p><span class="toggle" style="top:394px">+</span>
    <p class="q" style="top:452px">Processing time</p><span class="toggle" style="top:454px">+</span>
    <p class="q" style="top:510px">Im ready and want to apply - What next?</p><span class="toggle" style="top:512px">+</span>
  </section>

  <!-- footer -->
  <footer class="section footer">
    <h2 class="abs heading-dark" style="left:108px;top:74px;font-size:25px">THANKS &amp; KIND REGARDS</h2>
    <p class="abs" style="left:104px;top:130px;font-family:'Montserrat',sans-serif;font-weight:600;font-size:30px;color:var(--red)">MARC DELAUNAY</p>
    <p class="t t-ink" style="left:106px;top:176px">Visa Consultant</p>
    <div class="brand">BELLE ROUTE VISA</div>

    <div class="contact">
      <div class="contact-row" style="top:32px">
        <svg width="22" height="22" viewBox="0 0 24 24"><path d="M6.6 10.8a15 15 0 0 0 6.6 6.6l2.2-2.2c.3-.3.7-.4 1-.2 1.1.4 2.3.6 3.6.6.6 0 1 .4 1 1V20c0 .6-.4 1-1 1A17 17 0 0 1 3 4c0-.6.4-1 1-1h3.5c.6 0 1 .4 1 1 0 1.3.2 2.5.6 3.6.1.3 0 .7-.2 1z" fill="#fff"/></svg>
        <span>+44 (0) 100 200 3001/+44 (0) 200 300 4001</span>
      </div>
      <div class="contact-row" style="top:82px">
        <svg width="22" height="22" viewBox="0 0 24 24"><rect x="6" y="2" width="12" height="6" fill="#fff"/><rect x="2" y="9" width="20" height="9" rx="2" fill="#fff"/><rect x="6" y="15" width="12" height="7" fill="#fff" stroke="#f2504b" stroke-width="1.5"/></svg>
        <span>+44 (0) 100 200 3002/+44 (0) 200 300 4002</span>
      </div>
      <div class="contact-row" style="top:132px">
        <svg width="22" height="22" viewBox="0 0 24 24"><rect x="2" y="5" width="20" height="14" rx="2" fill="#fff"/><path d="M3 6l9 7 9-7" fill="none" stroke="#f2504b" stroke-width="1.8"/></svg>
        <span>hello@belleroutevisa.example</span>
      </div>
      <div class="contact-row" style="top:180px">
        <svg width="22" height="22" viewBox="0 0 24 24"><circle cx="12" cy="12" r="10" fill="#fff"/><path d="M2 12h20M12 2c3 3 3 17 0 20M12 2c-3 3-3 17 0 20" fill="none" stroke="#f2504b" stroke-width="1.4"/></svg>
        <span>www.belleroutevisa.example</span>
      </div>
      <div class="contact-row" style="top:230px">
        <svg width="22" height="24" viewBox="0 0 24 26"><path d="M12 1a8 8 0 0 0-8 8c0 6 8 15 8 15s8-9 8-15a8 8 0 0 0-8-8z" fill="#fff"/><circle cx="12" cy="9" r="3" fill="#f2504b"/></svg>
        <span>27 Harbour Lane Ground Floor<br>Westbury London NW9 4QE</span>
      </div>
    </div>

    <div class="footer-photo" role="img" aria-label="Black and white photo of an iron lattice tower rising above a city street"></div>
  </footer>

</main>
</body>
</html>
```